Business Card Design Project

Hello- I am an interior stylist/product designer whose work is detail driven, very clean and transitional in style and I want my business card to reflect those qualities. I have a logo that I use on my website- my name and a hand drawn chandelier that I want incorporated into the design. However, "Design for the Home" needs to be changed to "Designs". I will be using cream colored stock and am thinking of gray text and logo. I need your help in pulling my card together since it will be the most used element and drive the design of the rest of my stationary suite.
Updates

Please note that I have changed my QR code from my cell # to my website. The new code will be downloaded now.

Reason: I want to thank everyone who has submitted designs- there are truly some very inspiring designs and I am very pleased. I want to make certain that I get this right and have an attractive and highly effective marketing tool when we are finished. With that said, I have run into a technical problem with one aspect of the card- a qr code for my website that was not part of the original brief. I will get that corrected today and post. Once I get that taken care of, I will post comments to all designs received do far. Thanks again for everyone's efforts, Risa

QR Code for the website is now uploaded. Thanks for your patience!

Target Market(s)

Upper middle class- mostly women

Industry/Entity Type

Business

Requirements
Must have
• Marisa Vantry Designs
"...in every small touch."
214-555-0148
marisavantry@plumwick.net
www.marisavantrydesigns-example.com
27083 Birchmont Court
Dallas, TX 75000
Nice to have
• Risa Vantry
Owner

```html
<!DOCTYPE html>
<html lang="en">
<head>
<meta charset="utf-8">
<title>Marisa Vantry Designs — Business Card</title>
<link rel="stylesheet" href="https://fonts.googleapis.com/css2?family=Cormorant+Garamond:ital,wght@0,500;1,500&family=Marcellus&family=Open+Sans:wght@400&display=swap">
<style>
  :root {
    --backdrop: #e8e5de;
    --card-stock: #fbf5ab;
    --ink: #5b5e5c;
    --ink-soft: #6e7371;
    --rule: #b9b6a4;
    --card-shadow: rgba(40, 30, 20, 0.28);
  }
  * { margin: 0; padding: 0; box-sizing: border-box; }
  html, body {
    width: 1200px;
    height: 851px;
    overflow: hidden;
    background: var(--backdrop);
  }
  .canvas {
    position: relative;
    width: 1200px;
    height: 851px;
  }
  .card {
    position: absolute;
    width: 620px;
    height: 352px;
    background: var(--card-stock);
    box-shadow: 0 4px 14px var(--card-shadow);
    color: var(--ink);
  }
  .card--front { left: 96px; top: 60px; }
  .card--back { left: 540px; top: 470px; }

  /* Wordmark */
  .wordmark {
    font-family: "Cormorant Garamond", Georgia, serif;
    font-weight: 500;
    color: var(--ink);
    text-align: center;
    line-height: 1;
  }
  .wordmark__name { display: block; }
  .wordmark__sub {
    display: block;
    text-transform: uppercase;
    letter-spacing: 0.22em;
  }

  /* Front */
  .card--front .wordmark {
    position: absolute;
    left: 0; right: 0;
    top: 146px;
  }
  .card--front .wordmark__name { font-size: 40px; }
  .card--front .wordmark__sub { font-size: 14px; margin-top: 12px; }
  .tagline {
    position: absolute;
    left: 0; right: 0;
    top: 252px;
    text-align: center;
    font-family: "Cormorant Garamond", Georgia, serif;
    font-style: italic;
    font-weight: 500;
    font-size: 20px;
    color: var(--ink-soft);
  }

  /* Back */
  .card--back .wordmark {
    position: absolute;
    left: 36px;
    width: 220px;
    top: 172px;
  }
  .card--back .wordmark__name { font-size: 24px; }
  .card--back .wordmark__sub { font-size: 9px; margin-top: 8px; }
  .divider {
    position: absolute;
    left: 276px;
    top: 80px;
    width: 1px;
    height: 190px;
    background: var(--rule);
  }
  .contact {
    position: absolute;
    left: 304px;
    top: 84px;
  }
  .contact__name {
    font-family: "Marcellus", Georgia, serif;
    font-weight: 400;
    font-size: 26px;
    letter-spacing: 0.02em;
    line-height: 1;
  }
  .contact__role {
    font-family: "Open Sans", Arial, sans-serif;
    font-size: 14px;
    margin: 4px 0 0 62px;
    color: var(--ink-soft);
  }
  .contact__details {
    list-style: none;
    margin-top: 18px;
    font-family: "Open Sans", Arial, sans-serif;
    font-size: 15.5px;
    line-height: 20px;
    white-space: nowrap;
  }
</style>
</head>
<body>
<main class="canvas">
  <section class="card card--front" aria-label="Card front">
    <div class="wordmark">
      <span class="wordmark__name">Marisa Vantry</span>
      <span class="wordmark__sub">Designs</span>
    </div>
    <p class="tagline">"...in every small touch."</p>
  </section>

  <section class="card card--back" aria-label="Card back">
    <div class="wordmark">
      <span class="wordmark__name">Marisa Vantry</span>
      <span class="wordmark__sub">Designs</span>
    </div>
    <div class="divider"></div>
    <div class="contact">
      <h1 class="contact__name">RISA VANTRY</h1>
      <p class="contact__role">Owner</p>
      <ul class="contact__details">
        <li>214-555-0148</li>
        <li>marisavantry@plumwick.net</li>
        <li>www.marisavantrydesigns-example.com</li>
        <li>27083 Birchmont Court</li>
        <li>Dallas, TX 75000</li>
      </ul>
    </div>
  </section>
</main>
</body>
</html>
```